Design business card for Bright Harbour Coaching!

I am a personal development coach (like a life coach) and corporate trainer and need a professionally designed double sided business card.

It needs to contain the business logo (I'm happy for the designer to choose the layout of the logo as I am still working out the best option myself) and the following information:

Tamsin Varga
Personal Development Coach and Trainer

+61 (0)452 819 407 (written that way)
tamsin@bright-harbour.com

www.bright-harbour.com

```html
<!DOCTYPE html>
<html lang="en">
<head>
<meta charset="utf-8">
<title>Bright Harbour Coaching – Business Card</title>
<link rel="stylesheet" href="https://fonts.googleapis.com/css2?family=Tinos:wght@400;700&display=swap">
<style>
  :root {
    --teal: #0a93a3;
    --teal-dark: #066c78;
    --teal-deep: #055a64;
    --paper: #f4f4f4;
    --ink-grey: #5a5a5a;
    --white: #ffffff;
    --backdrop: #e6e8e9;
  }
  * { margin: 0; padding: 0; box-sizing: border-box; }
  html, body {
    width: 1200px; height: 716px; overflow: hidden;
    background: var(--backdrop);
    font-family: "Tinos", "Times New Roman", serif;
  }
  .sheet {
    position: relative; width: 1200px; height: 716px;
    display: flex; align-items: center; justify-content: center; gap: 40px;
  }
  .card {
    position: relative; width: 540px; height: 310px; overflow: hidden;
    box-shadow: 0 6px 18px rgba(0,0,0,0.18);
  }
  .card-shapes { position: absolute; inset: 0; }

  /* Front */
  .card-front { background: var(--paper); }
  .brand {
    position: absolute; left: 60px; top: 108px;
    display: flex; align-items: center; gap: 18px;
    color: var(--ink-grey); font-weight: 400;
  }
  .brand-mark {
    width: 34px; height: 34px; border-radius: 50%; background: var(--teal);
    flex: none;
  }
  .brand-name { font-size: 36px; letter-spacing: 1px; line-height: 1; text-transform: uppercase; }
  .brand-tagline { font-size: 20px; letter-spacing: 5px; line-height: 1.4; text-transform: uppercase; }

  /* Back */
  .card-back { background: var(--teal); color: var(--white); }
  .contact { position: absolute; left: 40px; top: 34px; }
  .contact-name { font-size: 24px; font-weight: 700; line-height: 1.1; }
  .contact-role { font-size: 11px; margin-top: 2px; }
  .contact-phone { font-size: 18px; margin-top: 14px; }
  .contact-email { font-size: 16px; margin-top: 10px; }
  .web-band {
    position: absolute; left: 0; top: 176px; width: 330px; height: 34px;
    background: linear-gradient(90deg, var(--white) 0%, rgba(255,255,255,0.85) 55%, rgba(255,255,255,0) 100%);
    color: var(--teal-deep); font-size: 19px; font-weight: 700;
    padding: 6px 0 0 40px;
  }
  .emblem {
    position: absolute; right: 60px; top: 120px;
    width: 130px; height: 130px; border-radius: 50%; background: var(--white);
  }
</style>
</head>
<body>
<main class="sheet">
  <section class="card card-front" aria-label="Business card front">
    <svg class="card-shapes" viewBox="0 0 540 310" aria-hidden="true">
      <polygon points="0,0 470,0 0,95" fill="var(--teal)"/>
      <polygon points="540,170 540,310 130,310" fill="var(--teal)"/>
      <polygon points="540,245 540,310 300,310" fill="var(--teal-dark)"/>
    </svg>
    <div class="brand">
      <span class="brand-mark" aria-hidden="true"></span>
      <div>
        <p class="brand-name">Bright Harbour</p>
        <p class="brand-tagline">Coaching &amp; Training</p>
      </div>
    </div>
  </section>

  <section class="card card-back" aria-label="Business card back">
    <svg class="card-shapes" viewBox="0 0 540 310" aria-hidden="true">
      <rect x="0" y="222" width="540" height="10" fill="var(--teal-dark)"/>
      <rect x="0" y="292" width="540" height="8" fill="var(--teal-dark)"/>
    </svg>
    <div class="contact">
      <p class="contact-name">Tamsin Varga</p>
      <p class="contact-role">Personal Development Coach and Trainer</p>
      <p class="contact-phone">+61 (0)452 819 407</p>
      <p class="contact-email">tamsin@bright-harbour.com</p>
    </div>
    <p class="web-band">www.bright-harbour.com</p>
    <span class="emblem" aria-hidden="true"></span>
  </section>
</main>
</body>
</html>
```